Kraft Eco-friendly pouch back imprint

Updating the design imprint on the back of our eco-friendly kraft stand up pouches. The current package back is a story letter but we want to change it to be more visually eye catching and make better use of buzzwords and graphics. I've uploaded a PDF with the current graphic so that key buzz words and thoughts could be pulled and highlighted.

The printing will be done in black and white, so don't spend time with colors. The imprint area is approximately 7" high x 5" wide.

I definitely want our logo at the top of the package, and I'm attaching two options.

Our mission is to be the Healthiest Pet Bakery in the U.S. That needs to be another point of emphasis.

Other potential buzzwords or bullets include:
Artisan Recipes
Simple Ingredients
No corn, wheat, soy, GMOs, or preservatives
Handcrafted
Locally sourced (Pacific NW)
Eco-conscious company
Updates

The system only allowed 24 hours. That is a ridiculously short time window.

Target Market(s)

Pet parents seeking natural, healthy products

Industry/Entity Type

independent pet channel

Colors

Designer to choose only greyscale colors for use in the design.

Requirements
Must have
• Logo, Mission, buzz words, graphics

```html
<!DOCTYPE html>
<html lang="en">
<head>
<meta charset="utf-8">
<title>Crumb &amp; Tail Bakery – Kraft Pouch Imprint</title>
<link rel="stylesheet" href="https://fonts.googleapis.com/css2?family=Amatic+SC:wght@700&family=Courier+Prime&family=Source+Sans+3:wght@600;700&display=swap">
<style>
  :root {
    --backdrop: #ececec;
    --kraft: #c89e76;
    --kraft-shade: #b98d65;
    --kraft-seam: #ad8259;
    --ink: #2b2420;
    --ink-soft: #4a3f38;
  }
  * { margin: 0; padding: 0; box-sizing: border-box; }
  html, body { width: 1200px; height: 800px; overflow: hidden; }
  body { background: var(--backdrop); position: relative; font-family: "Source Sans 3", sans-serif; color: var(--ink); }

  .pouch {
    position: absolute; top: 185px; width: 300px; height: 501px;
    background: var(--kraft); border-radius: 10px 10px 14px 14px;
  }
  .pouch--front { left: 280px; }
  .pouch--back { left: 641px; }
  .pouch__seal {
    position: absolute; left: 0; right: 0; top: 0; height: 62px;
    background: var(--kraft-shade); border-radius: 10px 10px 0 0;
    border-bottom: 2px solid var(--kraft-seam);
  }
  .pouch__notch {
    position: absolute; top: 20px; width: 6px; height: 8px; background: var(--backdrop);
  }
  .pouch__notch--left { left: 0; clip-path: polygon(0 0, 100% 50%, 0 100%); }
  .pouch__notch--right { right: 0; clip-path: polygon(100% 0, 0 50%, 100% 100%); }

  .centered { position: absolute; left: 0; right: 0; text-align: center; }

  .brand-mark { position: absolute; left: 50%; transform: translateX(-50%); }
  .brand-mark__ring {
    width: 50px; height: 50px; border: 2px solid var(--ink); border-radius: 50%; margin: 0 auto 6px;
  }
  .brand-mark__name {
    font-family: "Amatic SC", sans-serif; font-weight: 700; font-size: 34px; line-height: 0.95;
    color: var(--ink); white-space: nowrap; text-align: center;
  }
  .pouch--front .brand-mark { top: 121px; }
  .pouch--back .brand-mark { top: 348px; }

  .mission {
    top: 248px; font-family: "Amatic SC", sans-serif; font-weight: 700;
    font-size: 40px; line-height: 43px; letter-spacing: 1px; text-align: left; left: 48px;
  }

  .sourced-badge { position: absolute; left: 114px; top: 372px; }

  .tagline-serif { font-family: "Courier Prime", monospace; font-size: 11.5px; letter-spacing: 1px; }
  .tagline-sans { font-family: "Source Sans 3", sans-serif; font-weight: 700; font-size: 9.5px; letter-spacing: 1.2px; }
  .pouch--front .tagline-serif { top: 456px; }
  .pouch--front .tagline-sans { top: 473px; }

  .headline { top: 207px; font-weight: 700; font-size: 10.5px; letter-spacing: 1.2px; }
  .subhead { top: 225px; font-family: "Courier Prime", monospace; font-size: 10px; letter-spacing: 1px; }

  .free-list {
    position: absolute; top: 252px; left: 52px; right: 52px;
    display: flex; justify-content: space-between; list-style: none;
  }
  .free-list__item { width: 36px; text-align: center; }
  .free-list__item svg { display: block; margin: 0 auto 3px; }
  .free-list__label {
    font-family: "Source Sans 3", sans-serif; font-weight: 600; font-size: 6.5px; line-height: 7.5px;
    color: var(--ink-soft); text-transform: uppercase;
  }
  .free-list__label--small { font-size: 4.5px; }
</style>
</head>
<body>

<section class="pouch pouch--front">
  <div class="pouch__seal"></div>
  <span class="pouch__notch pouch__notch--left"></span>
  <span class="pouch__notch pouch__notch--right"></span>

  <div class="brand-mark">
    <div class="brand-mark__ring"></div>
    <div class="brand-mark__name">Crumb &amp; Tail<br>Bakery</div>
  </div>

  <h1 class="mission centered">Healthiest<br>Pet Bakery<br>in the U.S.</h1>

  <svg class="sourced-badge" width="72" height="72" viewBox="0 0 72 72" role="img" aria-label="Locally sourced Pacific Northwest stamp with pine trees">
    <circle cx="36" cy="36" r="34" fill="none" stroke="var(--ink)" stroke-width="2"/>
    <circle cx="36" cy="36" r="18" fill="var(--kraft-shade)"/>
  </svg>

  <p class="tagline-serif centered">HANDCRAFTED</p>
  <p class="tagline-sans centered">ECO-CONSCIOUS COMPANY</p>
</section>

<section class="pouch pouch--back">
  <div class="pouch__seal"></div>
  <span class="pouch__notch pouch__notch--left"></span>
  <span class="pouch__notch pouch__notch--right"></span>

  <p class="headline centered">SIMPLE INGREDIENTS</p>
  <p class="subhead centered">ARTISAN RECIPES</p>

  <ul class="free-list">
    <li class="free-list__item">
      <svg width="20" height="20" viewBox="0 0 20 20" aria-hidden="true"><circle cx="10" cy="10" r="8.5" fill="none" stroke="var(--ink)" stroke-width="1.5"/><ellipse cx="10" cy="10" rx="2.5" ry="5" fill="var(--ink)"/><line x1="4" y1="4" x2="16" y2="16" stroke="var(--ink)" stroke-width="1.5"/></svg>
      <span class="free-list__label">Corn<br>Free</span>
    </li>
    <li class="free-list__item">
      <svg width="20" height="20" viewBox="0 0 20 20" aria-hidden="true"><circle cx="10" cy="10" r="8.5" fill="none" stroke="var(--ink)" stroke-width="1.5"/><line x1="10" y1="5" x2="10" y2="15" stroke="var(--ink)" stroke-width="1.3"/><circle cx="8.5" cy="7" r="1.2" fill="var(--ink)"/><circle cx="11.5" cy="9" r="1.2" fill="var(--ink)"/><circle cx="8.5" cy="11" r="1.2" fill="var(--ink)"/><line x1="4" y1="4" x2="16" y2="16" stroke="var(--ink)" stroke-width="1.5"/></svg>
      <span class="free-list__label">Wheat<br>Free</span>
    </li>
    <li class="free-list__item">
      <svg width="20" height="20" viewBox="0 0 20 20" aria-hidden="true"><circle cx="10" cy="10" r="8.5" fill="none" stroke="var(--ink)" stroke-width="1.5"/><circle cx="7" cy="13" r="1.8" fill="none" stroke="var(--ink)"/><circle cx="10" cy="10" r="1.8" fill="none" stroke="var(--ink)"/><circle cx="13" cy="7" r="1.8" fill="none" stroke="var(--ink)"/><line x1="4" y1="4" x2="16" y2="16" stroke="var(--ink)" stroke-width="1.5"/></svg>
      <span class="free-list__label">Soy<br>Free</span>
    </li>
    <li class="free-list__item">
      <svg width="20" height="20" viewBox="0 0 20 20" aria-hidden="true"><circle cx="10" cy="10" r="8.5" fill="none" stroke="var(--ink)" stroke-width="1.5"/><path d="M7 4 Q13 10 7 16 M13 4 Q7 10 13 16" fill="none" stroke="var(--ink)" stroke-width="1.2"/><line x1="4" y1="4" x2="16" y2="16" stroke="var(--ink)" stroke-width="1.5"/></svg>
      <span class="free-list__label">GMO<br>Free</span>
    </li>
    <li class="free-list__item">
      <svg width="20" height="20" viewBox="0 0 20 20" aria-hidden="true"><circle cx="10" cy="10" r="8.5" fill="none" stroke="var(--ink)" stroke-width="1.5"/><path d="M8.5 5 H11.5 M9 5 V9 L6 14.5 H14 L11 9 V5" fill="none" stroke="var(--ink)" stroke-width="1.2"/><line x1="4" y1="4" x2="16" y2="16" stroke="var(--ink)" stroke-width="1.5"/></svg>
      <span class="free-list__label"><span class="free-list__label--small">Preservatives</span><br>Free</span>
    </li>
  </ul>

  <div class="brand-mark">
    <div class="brand-mark__ring"></div>
    <div class="brand-mark__name">Crumb &amp; Tail<br>Bakery</div>
  </div>
</section>

</body>
</html>
```